Kelmo bottle Label (Yoghurt drink)

Label for a 300 ml yoghurt drink bottle in 3 flavours.

General description:
• This is to design a sleeve shrink label for a Yoghurt Drink bottle in three flavours, Classic, Strawberry and Blueberry.
• Attached 3 photos: The one with KELMO brand in the current design we want to replace using the same bottle.
• Graphically, the design is to be similar to the examples provided for trevanu and fizzlotop.
• Use font and barcode size to be readable and legal.
• Minimize the use of the upper third of the bottle as it will be distorted when the label shrinks to the bottle.
• Professional and experienced designers only are welcome, please do not waste your time otherwise.

Bottle dimensions:
• Base across: 61 mm
• Height: 145 mm (approximate)

Graphical description:
• White colour with bands at the top and bottom similar to the one in “trevanu” example provided (not necessarily identical, feel free to be creative.
• The upper and lower bands to be: Green for “classic”, Pink or red for strawberry and purple for blueberry flavour.
• On the front: the brand name “Kelmo” and description “Yoghurt Drink” to be graphically attractive.
• On the front: two or more pieces of strawberry or blueberry for each flavour placed nicely with the option to include “yoghurt splash” or any suitable affects you deem suitable.
• For the Classic flavour, use the words (Classic, Lassi, Ayran) in the same location for the berries done in a graphically suitable manner.
• Colour temperature for the three flavours to be similar.

Information and objects on the label:
Front:
• The word “Kelmo” (brand name)
• “Yoghurt drink” (Product description)
• “300 ml” (size)
• Picture of Strawberries for strawberry flavour.
• Picture of Blueberries for blueberry flavour.
• The words (Classic, Lassi, Ayran) in the place used for the strawberries in the flavoured type, distributed to look graphically suitable for the overall design.

Back:
• Ingredient: Milk/milk solids, culture, salt, water, sugar, colour, flavour. (this is to be finalized later)
• Nutrition information table: (to be provided later).
• Barcode (to be provided later)
• Product of Australia
• Feluna Ristov Pty Ltd, 7/4 Corran Rd, Malaga, WA 6090
• info@kelmo-example.com.au 0491862037
• Keep under 5⁰ C
• Best before date printed on the bottle
• Shake well (to be located on the side at the top)
• Recycle icon.

Health benefits: (to be located suitably, possibly on the side with vertical orientation)
• Rich in probiotic bacteria and vitamins.
• Improves digestion and bowel motion.
• Supports weight control and fat loss.

Target Market(s)

General consumers

Industry/Entity Type

Grocery Store

Font styles to use
Sans Serif

Colors
abd037
b768aa
f04a50

Requirements
Must have
• The details in the project description
• The design must be simple and neat.
• Please use the shape of the current bottle "Kelmo" as in the attached photo.
Should not have
• Busy, cluttered, or empty and incomplete designs.

```html
<!DOCTYPE html>
<html lang="en">
<head>
<meta charset="utf-8">
<title>Kelmo Yoghurt Drink – Bottle Labels</title>
<link href="https://fonts.googleapis.com/css2?family=Raleway:wght@300;400;500;700&display=swap" rel="stylesheet">
<style>
  :root {
    --page-bg: #ffffff;
    --cap-dark: #a9a9a9;
    --cap-light: #ececec;
    --shoulder-mark: #c9c9cf;
    --blueberry: #5a2dbd;
    --blueberry-tint: #d9d9ee;
    --blueberry-photo-a: #2f3f86;
    --blueberry-photo-b: #7486c4;
    --classic: #22a046;
    --classic-tint: #d6eadb;
    --classic-photo-a: #3f8f2a;
    --classic-photo-b: #a7d46a;
    --strawberry: #c0268c;
    --strawberry-tint: #efd3de;
    --strawberry-photo-a: #c21f2b;
    --strawberry-photo-b: #f0605a;
  }
  * { box-sizing: border-box; margin: 0; padding: 0; }
  html, body {
    width: 1200px; height: 1200px; overflow: hidden;
    background: var(--page-bg);
    font-family: "Raleway", Arial, sans-serif;
  }
  .lineup { position: relative; width: 1200px; height: 1200px; }

  .bottle { position: absolute; top: 54px; width: 350px; height: 1020px; }
  .bottle--blueberry { left: 36px; --flavour: var(--blueberry); --tint: var(--blueberry-tint); --photo-a: var(--blueberry-photo-a); --photo-b: var(--blueberry-photo-b); }
  .bottle--classic { left: 424px; --flavour: var(--classic); --tint: var(--classic-tint); --photo-a: var(--classic-photo-a); --photo-b: var(--classic-photo-b); }
  .bottle--strawberry { left: 812px; --flavour: var(--strawberry); --tint: var(--strawberry-tint); --photo-a: var(--strawberry-photo-a); --photo-b: var(--strawberry-photo-b); }

  .bottle__body { position: absolute; inset: 0; width: 350px; height: 1020px; }
  .bottle__body .glass-top { stop-color: #ffffff; }
  .bottle__body .glass-bottom { stop-color: var(--tint); }

  .bottle__cap {
    position: absolute; left: 85px; top: 0; width: 180px; height: 84px;
    border-radius: 8px 8px 3px 3px;
    background: repeating-linear-gradient(90deg, var(--cap-dark) 0 3px, var(--cap-light) 3px 7px);
    box-shadow: inset 0 -10px 0 rgba(0,0,0,0.08);
  }

  .shoulder-name {
    position: absolute; top: 160px; left: 0; width: 350px; text-align: center;
    font-size: 11px; font-weight: 400; letter-spacing: 4px; color: var(--shoulder-mark);
  }

  .flavour-photo {
    position: absolute; left: 90px; top: 355px; width: 170px; height: 170px; border-radius: 50%;
    background: radial-gradient(circle at 40% 35%, var(--photo-b), var(--photo-a));
  }
  .flavour-ring {
    position: absolute; left: 75px; top: 340px; width: 200px; height: 200px; border-radius: 50%;
    border: 6px solid var(--flavour); opacity: 0.35;
  }

  .brand-stack {
    position: absolute; left: 110px; top: 548px; width: 130px; text-align: center;
    font-size: 104px; line-height: 88px; font-weight: 500; color: var(--flavour);
  }
  .brand-stack span { display: block; }

  .side-text {
    position: absolute; writing-mode: vertical-rl; transform: rotate(180deg);
    color: var(--flavour); white-space: nowrap;
  }
  .side-text--product { left: 82px; top: 620px; font-size: 25px; }
  .side-text--product strong { font-weight: 700; }
  .side-text--product .light { font-weight: 300; }
  .side-text--size { left: 238px; top: 690px; font-size: 21px; font-weight: 300; }
  .side-text--size .flavour-name { font-size: 25px; font-weight: 400; }
</style>
</head>
<body>
<main class="lineup">

  <section class="bottle bottle--blueberry">
    <svg class="bottle__body" viewBox="0 0 350 1020" aria-hidden="true">
      <defs>
        <linearGradient id="glass-blueberry" x1="0" y1="0" x2="0" y2="1">
          <stop offset="0.2" class="glass-top"/><stop offset="1" class="glass-bottom"/>
        </linearGradient>
      </defs>
      <path d="M95 80 L255 80 L255 150 C255 210 345 260 345 360 L345 985 Q345 1015 315 1015 L35 1015 Q5 1015 5 985 L5 360 C5 260 95 210 95 150 Z" fill="url(#glass-blueberry)" stroke="#e4e4ea" stroke-width="2"/>
    </svg>
    <div class="bottle__cap"></div>
    <p class="shoulder-name">KELMO</p>
    <div class="flavour-ring"></div>
    <div class="flavour-photo" role="img" aria-label="Fresh blueberries with a yoghurt splash"></div>
    <h1 class="brand-stack"><span>K</span><span>E</span><span>L</span><span>M</span><span>O</span></h1>
    <p class="side-text side-text--product"><strong>YOGHURT</strong> <span class="light">DRINK</span></p>
    <p class="side-text side-text--size">300 ML <span class="flavour-name">BLUEBERRY</span></p>
  </section>

  <section class="bottle bottle--classic">
    <svg class="bottle__body" viewBox="0 0 350 1020" aria-hidden="true">
      <defs>
        <linearGradient id="glass-classic" x1="0" y1="0" x2="0" y2="1">
          <stop offset="0.2" class="glass-top"/><stop offset="1" class="glass-bottom"/>
        </linearGradient>
      </defs>
      <path d="M95 80 L255 80 L255 150 C255 210 345 260 345 360 L345 985 Q345 1015 315 1015 L35 1015 Q5 1015 5 985 L5 360 C5 260 95 210 95 150 Z" fill="url(#glass-classic)" stroke="#e4e4ea" stroke-width="2"/>
    </svg>
    <div class="bottle__cap"></div>
    <p class="shoulder-name">KELMO</p>
    <div class="flavour-ring"></div>
    <div class="flavour-photo" role="img" aria-label="Green leaf with a yoghurt splash"></div>
    <h2 class="brand-stack"><span>K</span><span>E</span><span>L</span><span>M</span><span>O</span></h2>
    <p class="side-text side-text--product"><strong>YOGHURT</strong> <span class="light">DRINK</span></p>
    <p class="side-text side-text--size">300 ML <span class="flavour-name">CLASSIC</span></p>
  </section>

  <section class="bottle bottle--strawberry">
    <svg class="bottle__body" viewBox="0 0 350 1020" aria-hidden="true">
      <defs>
        <linearGradient id="glass-strawberry" x1="0" y1="0" x2="0" y2="1">
          <stop offset="0.2" class="glass-top"/><stop offset="1" class="glass-bottom"/>
        </linearGradient>
      </defs>
      <path d="M95 80 L255 80 L255 150 C255 210 345 260 345 360 L345 985 Q345 1015 315 1015 L35 1015 Q5 1015 5 985 L5 360 C5 260 95 210 95 150 Z" fill="url(#glass-strawberry)" stroke="#e4e4ea" stroke-width="2"/>
    </svg>
    <div class="bottle__cap"></div>
    <p class="shoulder-name">KELMO</p>
    <div class="flavour-ring"></div>
    <div class="flavour-photo" role="img" aria-label="Fresh strawberries with a yoghurt splash"></div>
    <h2 class="brand-stack"><span>K</span><span>E</span><span>L</span><span>M</span><span>O</span></h2>
    <p class="side-text side-text--product"><strong>YOGHURT</strong> <span class="light">DRINK</span></p>
    <p class="side-text side-text--size">300 ML <span class="flavour-name">STRAWBERRY</span></p>
  </section>

</main>
</body>
</html>
```